"Cork Hollow Excursions" is a top notch Santa Barbara County Wine Tour company.

We provide scenic, boutique and custom wine tours. I need the card to be clean and classy. I will provide our logo. I would like the logo to cover the back side of the card as an option and would like to see a couple color options other then our signature green and gold. I would like to see some creative options and let the designers come up with options.
I need cards for myself and my team. The final design should communicate "An authentic and boutique wine tour experience"
Please use my website for reference www.corkhollowexcursions.com

Target Market(s)

We have a wide range of clients from millennials to baby boomers

Industry/Entity Type

Tour

Contact Information for Business Card

Contact info:
Dale Munford
805-291-6384
info@corkhollowexcursions.com
corkhollowexcursions.com

Colors

Designer to choose colors to be used in the design.

Requirements
Must have
• my logo
Nice to have
• *I would like to have the backside side with the logo and the company statement
• "An authentic and boutique wine tour experience" as an option.
• *I would also like to see what the designers can create!
• *I would like to see an option that incorporates or social: snapgrid, rovia, route scout
Should not have
• I do not want it too busy.

```html
<!DOCTYPE html>
<html lang="en">
<head>
<meta charset="utf-8">
<title>Cork Hollow Excursions – Business Card</title>
<link href="https://fonts.googleapis.com/css2?family=EB+Garamond:ital,wght@0,500;0,600;1,400&family=Libre+Baskerville:wght@700&display=swap" rel="stylesheet">
<style>
  :root {
    --backdrop: #cdc9ca;
    --green: #0f2a1a;
    --green-deep: #0a2013;
    --gold: #cdb48f;
    --gold-light: #e4d3b6;
    --white: #ffffff;
    --ink: #14261a;
  }
  * { margin: 0; padding: 0; box-sizing: border-box; }
  html, body { width: 1200px; height: 800px; overflow: hidden; }
  body {
    background: var(--backdrop);
    position: relative;
    font-family: "EB Garamond", Georgia, serif;
  }
  .card {
    position: absolute;
    width: 525px;
    height: 300px;
    background: linear-gradient(135deg, var(--green) 0%, var(--green-deep) 100%);
    box-shadow: 0 6px 18px rgba(0,0,0,0.18);
    overflow: hidden;
  }

  /* Logo side */
  .card--logo { left: 50px; top: 290px; }
  .gold-band {
    position: absolute;
    left: 0; right: 0;
    top: 118px;
    height: 64px;
    background: var(--gold);
  }
  .gold-band::before {
    content: "";
    position: absolute;
    left: 0; right: 0;
    top: 12px; height: 40px;
    background: var(--green);
  }
  .gold-band::after {
    content: "";
    position: absolute;
    left: 0; right: 0;
    top: 30px; height: 3px;
    background: var(--white);
  }
  .logo-frame {
    position: absolute;
    left: 142px; top: 60px;
    width: 240px; height: 180px;
    background: var(--gold);
    padding: 10px;
  }
  .logo-panel {
    width: 100%; height: 100%;
    background: var(--white);
    display: flex;
    flex-direction: column;
    align-items: center;
    justify-content: center;
    gap: 12px;
    text-align: center;
  }
  .logo-dot {
    width: 46px; height: 46px;
    border-radius: 50%;
    background: var(--green);
  }
  .logo-name {
    font-family: "EB Garamond", Georgia, serif;
    font-weight: 600;
    font-size: 20px;
    letter-spacing: 2px;
    text-transform: uppercase;
    color: var(--green);
    line-height: 1.15;
  }

  /* Name side */
  .card--name {
    right: 50px; top: 190px;
    background: var(--gold);
    padding: 9px;
  }
  .card-inner {
    position: relative;
    width: 100%; height: 100%;
    background: linear-gradient(135deg, var(--green) 0%, var(--green-deep) 100%);
  }
  .name-box {
    position: absolute;
    left: 0; top: 36px;
    width: 292px; height: 110px;
    background: var(--white);
    display: flex;
    align-items: center;
    padding-left: 22px;
  }
  .person-name {
    font-family: "Libre Baskerville", Georgia, serif;
    font-weight: 700;
    font-size: 34px;
    color: var(--ink);
    letter-spacing: -0.5px;
  }
  .rule { position: absolute; background: var(--white); }
  .rule--top { left: 292px; right: 0; top: 48px; height: 3px; }
  .rule--under { left: 0; width: 292px; top: 158px; height: 3px; }
  .rule--divider { left: 310px; top: 140px; width: 3px; height: 112px; }
  .rule--bottom { left: 310px; right: 0; top: 252px; height: 3px; }
  .contact {
    position: absolute;
    left: 326px; top: 152px;
    right: 8px;
    color: var(--white);
    font-style: italic;
    font-size: 12.5px;
    line-height: 1.45;
    list-style: none;
  }
  .social {
    position: absolute;
    left: 326px; top: 214px;
    right: 8px;
    display: flex;
    flex-wrap: wrap;
    gap: 2px 9px;
    list-style: none;
    color: var(--white);
    font-size: 10.5px;
    letter-spacing: 0.3px;
  }
</style>
</head>
<body>

  <section class="card card--logo" aria-label="Card back with company name">
    <div class="gold-band"></div>
    <div class="logo-frame">
      <div class="logo-panel">
        <span class="logo-dot"></span>
        <span class="logo-name">Cork Hollow<br>Excursions</span>
      </div>
    </div>
  </section>

  <section class="card card--name" aria-label="Card front with contact details">
    <div class="card-inner">
      <div class="name-box">
        <h1 class="person-name">Dale Munford</h1>
      </div>
      <span class="rule rule--top"></span>
      <span class="rule rule--under"></span>
      <span class="rule rule--divider"></span>
      <span class="rule rule--bottom"></span>
      <ul class="contact">
        <li>T: 805-291-6384</li>
        <li>E: info@corkhollowexcursions.com</li>
        <li>W: www.corkhollowexcursions.com</li>
      </ul>
      <ul class="social">
        <li>friendloop</li>
        <li>chirpline</li>
        <li>snapgrid</li>
        <li>searchly</li>
        <li>rovia</li>
        <li>route scout</li>
      </ul>
    </div>
  </section>

</body>
</html>
```